Coffee House With Cycling Theme Wants Business Cards

We want to create a business card for a coffee house that has a cycling theme. We expect to use the current logo on one side of the business card and we have been considering adding the words 'COFFEE HOUSE' underneath (see example). For the other side of the business card we want an interesting design with tag-line, address and social media links (the normal business card stuff). See examples provided but we are not fixed on having it exactly as shown, we are very open to great creative ideas. Please note our logo has the initials ‘RM' in orange embedded in the design and this must be retained. However, you can play with the words COFFEE HOUSE as well as use the orange color on the backside of the business card, as you see fit. For an image on the backside of the business card it can be a photo, hand-drawn or whatever but it must visually combine coffee and cycling in some way. The interior of the Coffee House will be reclaimed wood, rustic and have an urban feel to it with cycling artifacts hanging from the walls/ceiling, etc. Finally, it would be beneficial if the business card design elements can be easily used on flyers and other promotional assets. Good luck, we are looking forward to seeing your creative ideas.

Target Market(s)

Coffee lovers and cycling fans

Contact Information for Business Card

See project description.

Colors

Designer to choose colors to be used in the design.

Requirements
Must have
• Must use the current logo provided and combine a coffee and bike theme.
Nice to have
• Orange is used in current logo and could be used as an accent color on the backside of the business card.

```html
<!DOCTYPE html>
<html lang="en">
<head>
<meta charset="utf-8">
<title>RM Coffee House – Business Card</title>
<link rel="stylesheet" href="https://fonts.googleapis.com/css2?family=Oswald:wght@400;500&family=Permanent+Marker&family=Gochi+Hand&display=block">
<style>
  :root {
    --orange: #ff6a13;
    --charcoal: #3d3d3d;
    --ink: #111111;
    --paper: #ffffff;
    --mug-tone: #f1f1f1;
  }
  * { box-sizing: border-box; margin: 0; padding: 0; }
  html, body { width: 750px; height: 1200px; overflow: hidden; background: var(--paper); }
  .canvas { position: relative; width: 750px; height: 1200px; background: var(--paper); }

  .side-label {
    position: absolute; right: 14px;
    font-family: "Gochi Hand", cursive;
    font-size: 34px; color: var(--ink); letter-spacing: 1px;
  }
  .side-label--front { top: 40px; }
  .side-label--back { top: 580px; }

  .front-card { position: absolute; left: 0; top: 100px; width: 750px; height: 460px; }
  .stripe { position: absolute; top: 12px; height: 425px; background: var(--orange); }
  .stripe--thin { left: 67px; width: 21px; }
  .stripe--wide { left: 117px; width: 33px; }

  .brand {
    position: absolute; left: 250px; top: 130px; width: 400px;
    text-align: center;
  }
  .brand-name {
    font-family: "Oswald", sans-serif; font-weight: 500;
    font-size: 118px; line-height: 1; color: var(--charcoal);
    display: inline-flex; align-items: center; gap: 16px;
  }
  .brand-dot { width: 26px; height: 26px; border-radius: 50%; background: var(--orange); }
  .brand-tagline {
    margin-top: 14px;
    font-family: "Oswald", sans-serif; font-weight: 400;
    font-size: 42px; letter-spacing: 1px; color: var(--ink);
  }

  .back-card {
    position: absolute; left: 0; top: 657px; width: 750px; height: 430px;
    background: var(--orange);
  }
  .slogan {
    position: absolute; left: 62px; top: 50px;
    font-family: "Permanent Marker", "Gochi Hand", cursive;
    font-size: 30px; line-height: 1; letter-spacing: 2px; color: var(--ink);
    text-transform: uppercase;
  }
  .mug-art {
    position: absolute; left: 62px; top: 118px; width: 275px; height: 275px;
    border-radius: 18px;
    background: linear-gradient(160deg, #ffffff 0%, var(--mug-tone) 70%, #dcdcdc 100%);
  }
  .social-list { position: absolute; left: 362px; top: 170px; list-style: none; }
  .social-item {
    display: flex; align-items: center; gap: 14px; height: 57px;
    font-family: "Gochi Hand", cursive; font-size: 31px; color: var(--ink);
  }
  .social-marker { width: 30px; height: 30px; background: var(--ink); border-radius: 4px; }
  .social-marker--round { border-radius: 50%; }
</style>
</head>
<body>
<main class="canvas">
  <span class="side-label side-label--front">front</span>

  <section class="front-card">
    <div class="stripe stripe--thin"></div>
    <div class="stripe stripe--wide"></div>
    <div class="brand">
      <div class="brand-name">RM<span class="brand-dot"></span></div>
      <div class="brand-tagline">COFFEE HOUSE</div>
    </div>
  </section>

  <span class="side-label side-label--back">back</span>

  <section class="back-card">
    <p class="slogan">Grind on, pedal on</p>
    <div class="mug-art" role="img" aria-label="Illustration of a white coffee mug with a hand-drawn bicycle on it"></div>
    <ul class="social-list">
      <li class="social-item"><span class="social-marker"></span>rmcoffeehouse</li>
      <li class="social-item"><span class="social-marker"></span>rmcoffeehouse</li>
      <li class="social-item"><span class="social-marker social-marker--round"></span>rmcoffeehouse.com</li>
    </ul>
  </section>
</main>
</body>
</html>
```